Lawn mowing business card design

We need a business card design for our lawn mowing and gardening business which is located in the Northern Beaches of Sydney. Our business name is Copperleaf Yards and our logo is predominantly green and yellow in color. Please see our website at www.copperleafyards.com.au for design ideas. The business targets young professionals and older clientele. As such the font should be easy to read, but I also want the business card to be colorful and stand out.

Target Market(s)

young professionals

Industry/Entity Type

Lawn Care

Contact Information for Business Card

Copperleaf Yards, Martin Kealey, 0478650912, www.copperleafyards.com.au, email: copperleafyards@mailbox-example.com

Font styles to use
Serif

Colors
9bcb3b
fbed22

Requirements
Must have
• Must include the details listed above. Must include the attached logo.
Nice to have
• Logo attached with two copies. The logo without any writing is high quality, please feel free to be creative with the text stating our business name "Copperleaf Yards" using this file.

```html
<!DOCTYPE html>
<html lang="en">
<head>
<meta charset="utf-8">
<title>Copperleaf Yards – Business Cards</title>
<link rel="stylesheet" href="https://fonts.googleapis.com/css2?family=Marcellus&display=swap">
<style>
  :root {
    --leaf-green: #9bcb3b;
    --sun-yellow: #fbed22;
    --deep-green: #2f9a3c;
    --card-black: #060606;
    --card-white: #f7f7f7;
    --ink: #1c1c1c;
    --backdrop: #e6e4df;
  }
  * { box-sizing: border-box; margin: 0; padding: 0; }
  html, body {
    width: 1200px; height: 780px; overflow: hidden;
    background: var(--backdrop);
    font-family: "Marcellus", serif;
  }
  .stage {
    position: relative; width: 1200px; height: 780px;
    display: flex; align-items: center; justify-content: center; gap: 50px;
  }
  .card {
    position: relative; width: 525px; height: 300px;
    background: var(--card-white); overflow: hidden;
    box-shadow: 0 6px 18px rgba(0,0,0,.18);
  }
  .card-shapes { position: absolute; inset: 0; width: 100%; height: 100%; }

  /* front */
  .front-details {
    position: absolute; top: 22px; left: 150px; right: 26px;
    color: #fff;
  }
  .company-name {
    color: var(--leaf-green); font-size: 25px; letter-spacing: .5px;
    text-transform: uppercase; line-height: 1; font-weight: 400;
  }
  .company-tagline { font-size: 13px; margin-top: 3px; }
  .person-name {
    color: var(--leaf-green); font-size: 27px; margin-top: 18px; margin-left: 120px; line-height: 1.15;
  }
  .contact-list {
    list-style: none; margin-top: 12px; text-align: right; font-size: 13px; line-height: 1.5;
  }
  .contact-list .label { color: #fff; }
  .contact-list .value { color: var(--leaf-green); }
  .contact-list .web { color: #fff; }

  .brand-mark {
    position: absolute; display: flex; align-items: center; gap: 10px;
  }
  .brand-dot {
    width: 30px; height: 30px; border-radius: 50%; background: var(--leaf-green);
  }
  .brand-name { font-size: 24px; color: var(--ink); }
  .front .brand-mark { left: 36px; bottom: 30px; }

  /* back */
  .back .brand-mark { left: 190px; top: 130px; }
  .back-band {
    position: absolute; top: 0; bottom: 0; left: 46px; width: 22px; background: var(--leaf-green);
  }
  .back-web {
    position: absolute; left: 78px; top: 50%;
    transform: translate(-50%, -50%) rotate(-90deg) translateY(16px);
    transform-origin: center; font-size: 14px; color: var(--ink); white-space: nowrap;
  }
</style>
</head>
<body>
<main class="stage">
  <section class="card front" aria-label="Business card front">
    <svg class="card-shapes" viewBox="0 0 525 300" preserveAspectRatio="none" aria-hidden="true">
      <path d="M0 0 H525 V220 H300 C200 220 190 105 90 105 H0 Z" fill="var(--card-black)"/>
      <path d="M90 105 C190 105 200 220 300 220 H525 V232 H300 C195 232 185 117 90 117 H0 V105 Z" fill="var(--leaf-green)"/>
    </svg>
    <div class="front-details">
      <h1 class="company-name">Copperleaf Yards</h1>
      <p class="company-tagline">Lawns and Garden Maintenance</p>
      <p class="person-name">Martin Kealey</p>
      <ul class="contact-list">
        <li><span class="label">P: </span><span class="value">0478650912</span></li>
        <li><span class="label">E: </span><span class="value">copperleafyards@mailbox-example.com</span></li>
        <li class="web">www.copperleafyards.com.au</li>
      </ul>
    </div>
    <div class="brand-mark">
      <span class="brand-dot"></span>
      <span class="brand-name">Copperleaf Yards</span>
    </div>
  </section>

  <section class="card back" aria-label="Business card back">
    <div class="back-band"></div>
    <p class="back-web">www.copperleafyards.com.au</p>
    <div class="brand-mark">
      <span class="brand-dot"></span>
      <span class="brand-name">Copperleaf Yards</span>
    </div>
  </section>
</main>
</body>
</html>
```